Design a Shirt Hang Tag for a brand new streetwear company

We need a hang tag for our apparel. This will be attached and shipper with every shirt, hat, and hoodie. We make streetwear/urban apparel. For a feel of our products see http://loomferal.co

We'd like to see something die cut with a shape that isn't a rectangle.
Looking for a design that embodies "Savage". We are looking for something bold and fun. Our colors usually consist of black. white, and red, but if you feel like doing something else that you feel could fit our brand,go for it. Were savage, we don't want normal.

Target Market(s)

inner city, age 13-29, multi-cultural

Industry/Entity Type

Clothing

Font styles to use
Sans Serif
Other font styles liked:
• artist's choice

Colors
ec1f27
ffffff
000000

Requirements
Must have
• site url: www.loomferal.co
• Band Name: Loom Feral
• Double sided tag
• Die cut design

```html
<!DOCTYPE html>
<html lang="en">
<head>
<meta charset="utf-8">
<title>Loom Feral Hang Tag</title>
<link href="https://fonts.googleapis.com/css2?family=Lato:wght@300&family=Oswald:wght@600&display=swap" rel="stylesheet">
<style>
  :root {
    --bg: #ececec;
    --red: #dc2a2a;
    --white: #ffffff;
    --street-pink: #e77aa8;
    --street-blue: #4aa3d8;
    --street-yellow: #e9c94a;
    --street-purple: #7a6bc4;
    --street-orange: #e8552f;
  }
  html, body { margin: 0; padding: 0; overflow: hidden; }
  body { width: 1200px; height: 1041px; background: var(--bg); }
  .sheet { display: block; width: 1200px; height: 1041px; }
  .side-label { font-family: "Lato", sans-serif; font-weight: 300; font-size: 46px; fill: var(--red); letter-spacing: 1px; }
  .brand-name { font-family: "Oswald", sans-serif; font-weight: 600; fill: var(--white); letter-spacing: 2px; }
  .site-url { font-family: "Oswald", sans-serif; font-weight: 600; font-size: 14px; fill: var(--red); letter-spacing: 1px; }
</style>
</head>
<body>
<svg class="sheet" viewBox="0 0 1200 1041" xmlns="http://www.w3.org/2000/svg">
  <defs>
    <path id="tag-outline" d="M332,68 c-14,0 -20,10 -20,22 l-90,32 l-40,50 l-20,40 l-12,110 l0,60 c0,120 60,220 182,266 c122,-46 182,-146 182,-266 l0,-60 l-12,-110 l-20,-40 l-40,-50 l-90,-32 c0,-12 -6,-22 -20,-22z"/>
    <linearGradient id="street-art" x1="0" y1="0" x2="1" y2="1">
      <stop offset="0" stop-color="var(--street-yellow)"/>
      <stop offset="0.3" stop-color="var(--street-pink)"/>
      <stop offset="0.55" stop-color="var(--street-orange)"/>
      <stop offset="0.8" stop-color="var(--street-blue)"/>
      <stop offset="1" stop-color="var(--street-purple)"/>
    </linearGradient>
    <clipPath id="front-clip"><use href="#tag-outline"/></clipPath>
    <clipPath id="back-clip"><use href="#tag-outline" transform="translate(537 0)"/></clipPath>
  </defs>

  <text class="side-label" x="74" y="86">FRONT</text>
  <text class="side-label" x="1138" y="86" text-anchor="end">BACK</text>

  <!-- Front side -->
  <g class="tag-front">
    <g clip-path="url(#front-clip)">
      <rect x="140" y="60" width="390" height="600" fill="url(#street-art)" role="img" aria-label="Colourful street graffiti wall artwork"/>
      <path class="crest" d="M140,60 H530 V300 C470,300 400,306 332,318 C264,306 194,300 140,300Z" fill="var(--red)"/>
    </g>
    <use href="#tag-outline" fill="none" stroke="var(--red)" stroke-width="3"/>
    <circle class="hang-hole" cx="332" cy="86" r="7" fill="var(--white)"/>
    <text class="brand-name" x="332" y="258" font-size="48" text-anchor="middle" textLength="270" lengthAdjust="spacingAndGlyphs">LOOM FERAL</text>

    <g class="inner-shield">
      <path d="M240,316 H424 V552 L332,612 L240,552Z" fill="var(--white)" stroke="var(--red)" stroke-width="4"/>
      <rect x="254" y="330" width="156" height="170" fill="var(--red)" opacity="0.85" role="img" aria-label="Silhouettes of a woman and a man posing in streetwear"/>
      <line x1="248" y1="508" x2="416" y2="508" stroke="var(--red)" stroke-width="2"/>
      <text class="site-url" x="332" y="525" text-anchor="middle" textLength="150" lengthAdjust="spacingAndGlyphs">WWW.LOOMFERAL.CO</text>
      <rect x="250" y="532" width="164" height="30" fill="var(--red)"/>
      <text class="brand-name" x="332" y="554" font-size="19" text-anchor="middle" textLength="120" lengthAdjust="spacingAndGlyphs">LOOM FERAL</text>
    </g>
  </g>

  <!-- Back side -->
  <g class="tag-back">
    <g clip-path="url(#back-clip)">
      <rect x="677" y="60" width="390" height="600" fill="url(#street-art)" role="img" aria-label="Colourful abstract graffiti mural"/>
      <rect class="name-band" x="677" y="344" width="390" height="188" fill="var(--red)"/>
      <line x1="677" y1="344" x2="1067" y2="344" stroke="var(--white)" stroke-width="4"/>
      <line x1="677" y1="532" x2="1067" y2="532" stroke="var(--white)" stroke-width="4"/>
    </g>
    <use href="#tag-outline" transform="translate(537 0)" fill="none" stroke="var(--red)" stroke-width="3"/>
    <circle class="hang-hole" cx="869" cy="86" r="7" fill="var(--white)"/>
    <text class="brand-name" x="869" y="459" font-size="56" text-anchor="middle" textLength="290" lengthAdjust="spacingAndGlyphs">LOOM FERAL</text>
  </g>
</svg>
</body>
</html>
```